Business Card Design Project

We need a business card design for an existing company in Dallas/Fort Worth that is expanding services and re-branding. We are changing the name from Bristow Commercial Cleaning to Kelmont Facility Services. We are expanding from only commercial cleaning to include complete commercial landscape and facility maintenance services, too.

As stated, we offer a package of services that includes landscape, janitorial and facility services, which is largely unique in the industry.

We would like a design that communicates trust/partnership with a professional, corporate image, but not necessarily using the standard white business card. We would like a design that perhaps uses darker blues or perhaps a gray background, but we are open to other ideas. We might also be interested in a double-sided design - maybe with our logo on the back, printed on a gray background?

We will probably stick with the attached logo, but if you've got another inspired idea....

Target Market(s)

Property managers, commercial real estate professionals, corporate executives

Industry/Entity Type

Landscape

Requirements
Should not have
• Not interested in old style fonts.

```html
<!DOCTYPE html>
<html lang="en">
<head>
<meta charset="utf-8">
<title>Kelmont Facility Services – Business Card</title>
<link rel="stylesheet" href="https://fonts.googleapis.com/css2?family=Questrial&family=Arimo:ital,wght@0,400;1,400&display=swap">
<style>
  :root {
    --frame: #000000;
    --sheet: #ffffff;
    --card-center: #3c3c3c;
    --card-edge: #050505;
    --ink: #ffffff;
  }
  html, body {
    margin: 0;
    padding: 0;
    width: 1041px;
    height: 1200px;
    overflow: hidden;
    background: var(--frame);
  }
  .board {
    position: relative;
    width: 1041px;
    height: 1200px;
    background: var(--frame);
  }
  .sheet {
    position: absolute;
    left: 41px;
    top: 34px;
    width: 958px;
    height: 1125px;
    background: var(--sheet);
  }
  .card-face {
    position: absolute;
    background: radial-gradient(ellipse at 50% 45%, var(--card-center) 0%, #1a1a1a 45%, var(--card-edge) 100%);
    color: var(--ink);
  }
  .card-front {
    left: 84px;
    top: 81px;
    width: 866px;
    height: 496px;
  }
  .brand {
    position: absolute;
    left: 79px;
    top: 71px;
    width: 706px;
    height: 130px;
  }
  .brand-square {
    position: absolute;
    left: 0;
    top: 0;
    width: 104px;
    height: 104px;
    border: 7px solid var(--ink);
  }
  .brand-name {
    position: absolute;
    left: 130px;
    top: -12px;
    margin: 0;
    font-family: "Questrial", "Century Gothic", sans-serif;
    font-weight: 400;
    color: var(--ink);
    line-height: 1;
  }
  .brand-name .primary {
    display: block;
    font-size: 76px;
    letter-spacing: 6px;
  }
  .brand-name .secondary {
    display: block;
    font-size: 48px;
    letter-spacing: 3.4px;
    margin-top: 4px;
  }
  .tagline {
    position: absolute;
    left: 132px;
    top: 108px;
    margin: 0;
    font-family: "Arimo", Arial, sans-serif;
    font-style: italic;
    font-size: 17.5px;
    color: var(--ink);
    white-space: nowrap;
  }
  .contact {
    position: absolute;
    left: 35px;
    top: 263px;
    margin: 0;
    font-family: "Arimo", Arial, sans-serif;
    font-size: 24px;
    line-height: 30.8px;
    font-style: normal;
    color: var(--ink);
    white-space: nowrap;
  }
  .person {
    position: absolute;
    right: 16px;
    top: 244px;
    text-align: right;
    font-family: "Arimo", Arial, sans-serif;
    color: var(--ink);
  }
  .person-name {
    margin: 0;
    font-size: 47px;
    font-weight: 400;
    line-height: 1.1;
    text-decoration: underline;
    text-decoration-thickness: 2px;
    text-underline-offset: 5px;
  }
  .person-title {
    margin: 6px 10px 0 0;
    font-size: 25px;
    font-style: italic;
  }
  .card-back-mount {
    position: absolute;
    left: 79px;
    top: 611px;
    width: 868px;
    height: 495px;
    background: var(--frame);
  }
  .card-back-rule {
    position: absolute;
    left: 14px;
    top: 14px;
    right: 14px;
    bottom: 14px;
    border: 10px solid var(--sheet);
  }
  .card-back {
    left: 35px;
    top: 34px;
    width: 802px;
    height: 430px;
    display: flex;
    align-items: center;
    justify-content: center;
  }
  .back-name {
    margin: 0;
    font-family: "Questrial", "Century Gothic", sans-serif;
    font-weight: 400;
    font-size: 64px;
    letter-spacing: 5px;
    color: var(--ink);
    text-align: center;
    line-height: 1.15;
  }
</style>
</head>
<body>
  <main class="board">
    <div class="sheet"></div>

    <section class="card-face card-front" aria-label="Business card front">
      <div class="brand">
        <div class="brand-square" aria-hidden="true"></div>
        <h1 class="brand-name">
          <span class="primary">KELMONT</span>
          <span class="secondary">FACILITY SERVICES</span>
        </h1>
        <p class="tagline">One Source For Landscape, Janitorial and Facility Maintenance</p>
      </div>

      <address class="contact">
        Streetname 123<br>
        1234 Dallas, FW<br>
        T.&nbsp; 00 000 00 00<br>
        F.&nbsp; 00 000 00 00<br>
        E.&nbsp; info@kelmontfs.com<br>
        W. www.kelmontfacilityservices.com
      </address>

      <div class="person">
        <h2 class="person-name">Grant Whitfield</h2>
        <p class="person-title">General Manager</p>
      </div>
    </section>

    <section class="card-back-mount" aria-label="Business card back">
      <div class="card-back-rule"></div>
      <div class="card-face card-back">
        <p class="back-name">KELMONT</p>
      </div>
    </section>
  </main>
</body>
</html>
```